Business Card Design for Consulting Company

I require a Business Card design for my Consulting company. <br/><br/>My company name is: Marek Olvani Consulting Inc.<br/>My website is: www.marekolvaniconsulting.example<br/><br/>My company focuses on management and software development for the Tallobrix CRM platform (www.tallobrix.example)<br/><br/>I have a logo already designed...see attached.
Updates

Also Include my Name and Title: Marek T.L. Olvani President

Target Market(s)

Tallobrix Customers

Contact Information for Business Card

Only include my LOGO (provided)
My Name: Marek TL Olvani
My Title: President
My Company Name: Marek Olvani Consulting Inc.
My Website: www.marekolvaniconsulting.example
My Email: marek.olvani.consulting@mailbox.example

NO PHONE NUMBER
NO ADDRESS

Font styles to use
Serif
Sans Serif
Other font styles liked:
• see my website: www.marekolvaniconsulting.example

Colors

Designer to choose colors to be used in the design.

Requirements
Must have
• Must include my Orange
• Include my name (Marek T.L. Olvani), title (President) company name, website and email
• It should also have a tag line like: Tallobrix Consulting
• I'm flexible with the tag line
Should not have
• Don't include my phone number or address

```html
<!DOCTYPE html>
<html lang="en">
<head>
<meta charset="utf-8">
<title>Marek Olvani Consulting Inc. – Business Card</title>
<link rel="stylesheet" href="https://fonts.googleapis.com/css2?family=Lato:wght@400;700&display=swap">
<style>
  :root {
    --backdrop: #d8cfc3;
    --card-frost: #ece7e0;
    --card-edge: #f7f3ee;
    --panel-dark: #1c1c1c;
    --panel-mid: #2b2b2b;
    --orange: #d26a1e;
    --orange-light: #e07f2c;
    --text-light: #d9d6d2;
    --text-muted: #bdb8b2;
  }
  * { margin: 0; padding: 0; box-sizing: border-box; }
  html, body {
    width: 1200px;
    height: 1047px;
    overflow: hidden;
    background: var(--backdrop);
    font-family: "Lato", "Helvetica Neue", Arial, sans-serif;
  }
  .card {
    position: absolute;
    left: 100px;
    top: 254px;
    width: 1000px;
    height: 540px;
  }
  .card-shape {
    position: absolute;
    inset: 0;
  }
  .identity {
    position: absolute;
    left: 40px;
    top: 120px;
  }
  .identity .name {
    font-weight: 700;
    font-size: 44px;
    letter-spacing: 0.5px;
    color: var(--orange);
    text-transform: uppercase;
    line-height: 1;
  }
  .identity .title {
    margin-top: 10px;
    font-size: 21px;
    letter-spacing: 1.5px;
    color: var(--text-muted);
  }
  .contact {
    position: absolute;
    left: 40px;
    top: 292px;
  }
  .contact .company {
    font-weight: 700;
    font-size: 22px;
    color: var(--orange);
    margin-bottom: 18px;
  }
  .contact .line {
    display: flex;
    align-items: center;
    gap: 16px;
    font-size: 21px;
    color: var(--text-light);
    height: 33px;
  }
  .contact .line svg { flex: none; }
  .contact .accent { color: var(--orange-light); }
  .brand {
    position: absolute;
    left: 560px;
    top: 232px;
    width: 390px;
    display: flex;
    align-items: center;
    justify-content: center;
    gap: 18px;
  }
  .brand .mark {
    width: 30px;
    height: 30px;
    background: var(--orange);
    border-radius: 4px;
  }
  .brand .wordmark {
    font-weight: 700;
    font-size: 48px;
    color: var(--orange);
    letter-spacing: 0.5px;
  }
</style>
</head>
<body>
  <div class="card">
    <svg class="card-shape" width="1000" height="540" viewBox="0 0 1000 540" aria-hidden="true">
      <defs>
        <clipPath id="card-outline">
          <path d="M60,0 H990 Q1000,0 1000,10 V470 Q1000,540 930,540 H4 Q0,540 0,536 V60 Q0,0 60,0 Z"/>
        </clipPath>
        <linearGradient id="panel-fill" x1="0" y1="0" x2="1" y2="1">
          <stop offset="0" stop-color="var(--panel-mid)"/>
          <stop offset="1" stop-color="var(--panel-dark)"/>
        </linearGradient>
      </defs>
      <g clip-path="url(#card-outline)">
        <rect width="1000" height="540" fill="var(--card-frost)"/>
        <path d="M0,0 H545 Q440,270 545,540 H0 Z" fill="url(#panel-fill)"/>
        <path d="M553,0 Q446,270 553,540" fill="none" stroke="var(--orange)" stroke-width="5"/>
      </g>
      <path d="M60,0 H990 Q1000,0 1000,10 V470 Q1000,540 930,540 H4 Q0,540 0,536 V60 Q0,0 60,0 Z" fill="none" stroke="var(--card-edge)" stroke-width="2"/>
    </svg>

    <div class="identity">
      <div class="name">Marek TL Olvani</div>
      <div class="title">President</div>
    </div>

    <div class="contact">
      <div class="company">Marek Olvani Consulting Inc.</div>
      <div class="line">
        <svg width="20" height="15" viewBox="0 0 20 15" aria-hidden="true">
          <rect x="1" y="1" width="18" height="13" fill="none" stroke="var(--orange)" stroke-width="2"/>
          <path d="M1,1 L10,8 L19,1" fill="none" stroke="var(--orange)" stroke-width="2"/>
        </svg>
        <span>marek.olvani.consulting@mailbox.example</span>
      </div>
      <div class="line">
        <svg width="20" height="20" viewBox="0 0 20 20" aria-hidden="true">
          <circle cx="10" cy="10" r="8.5" fill="none" stroke="var(--orange)" stroke-width="1.6"/>
          <ellipse cx="10" cy="10" rx="3.8" ry="8.5" fill="none" stroke="var(--orange)" stroke-width="1.4"/>
          <path d="M1.5,10 H18.5 M3,5.5 H17 M3,14.5 H17" stroke="var(--orange)" stroke-width="1.4"/>
        </svg>
        <span>www.<span class="accent">marekolvaniconsulting</span>.example</span>
      </div>
    </div>

    <div class="brand">
      <span class="mark"></span>
      <span class="wordmark">Marek Olvani</span>
    </div>
  </div>
</body>
</html>
```